Keepers of the Crooked Teacup Order Book and ebook cover

The goal out of this is to make 1) a cover for a 5"x8" 170 page book, and then 2) an E book square high resolution cover to be used on Lorvantis.

I've attached the files that won the first competition on the book cover - for reference.

This book is called "Keepers of the crooked teacup order" - part 1
It is a comedy/satire about MBAs, education, and a bit of the current environment humor.

I want some thing of this style, but improved/better for this professional, informative, satire, and laugh out loud funny book.
Updates

I plan on extending the deadline for folks since I've seen a lot of intent to submit. Also to allow folks the weekend to work. Lots of good submittals

Target Market(s)

The book is a comedy satire. It is poking fun at people and the value of a masters in business administration. It is also using current comedy to augment it.(such at toilet paper shortages) ..example: is also a chapter on Examples of who is a keeper of the crooked teacup order and why. There are also examples showing how you can become a keeper of the crooked teacup order.

Requirements
Must have
• 1) Must have the logo on the back of the book in the corner.
2) must have the Author name on front: R.J. Wollstead
3) These are the words for the back of the book:
This is a comedy. Well, more a satire if you are going to split hairs, but stop being a smarty-pants.
Step 1: Start drinking. This book is better that way.
Step 2: Go poop.
Step 3: ?????
Step 4: Profit!
"This is a must read!"
(or at least a great gag gift for your best bullshitting friends and family.)
"Laugh out loud funny!"
"No one is safe!"

```html
<!DOCTYPE html>
<html lang="en">
<head>
<meta charset="utf-8">
<title>Keepers of the Crooked Teacup Order — Cover Wrap</title>
<link rel="stylesheet" href="https://fonts.googleapis.com/css2?family=Oswald:wght@400;500;600&family=Bitter:wght@700&family=Montserrat:wght@500;600&display=swap">
<style>
  :root {
    --back-dark: #45483a;
    --back-mid: #6a6d56;
    --back-light: #878a72;
    --spine: #5a6a38;
    --front-light: #e4e3d8;
    --front-mid: #b3b6a6;
    --front-dark: #4a5144;
    --shelf: #d9dad2;
    --shelf-shadow: #7c8176;
    --paper-light: #eeede4;
    --paper-mid: #cfcebf;
    --title-red: #c9261b;
    --accent-yellow: #e6d42a;
    --white: #ffffff;
    --logo-navy: #2c3b86;
  }
  html, body {
    margin: 0;
    padding: 0;
    width: 1200px;
    height: 924px;
    overflow: hidden;
    background: #2a2b24;
  }
  .cover-wrap {
    position: relative;
    width: 1200px;
    height: 924px;
    overflow: hidden;
  }

  /* ---------- Back cover ---------- */
  .back-cover {
    position: absolute;
    left: 0; top: 0;
    width: 578px; height: 924px;
  }
  .back-photo {
    position: absolute; inset: 0;
    background:
      linear-gradient(180deg, rgba(0,0,0,0) 0%, rgba(0,0,0,0) 68%, rgba(255,255,255,0.08) 70%, rgba(255,255,255,0.08) 82%, rgba(0,0,0,0.12) 84%, rgba(0,0,0,0.2) 100%),
      radial-gradient(ellipse at 35% 45%, var(--back-light) 0%, var(--back-mid) 50%, var(--back-dark) 100%);
  }
  .back-title {
    position: absolute;
    left: 0; width: 578px;
    top: 196px;
    margin: 0;
    text-align: center;
    font-family: 'Oswald', sans-serif;
    font-weight: 500;
    font-size: 34px;
    letter-spacing: -0.3px;
    color: var(--accent-yellow);
    text-transform: uppercase;
  }
  .back-intro {
    position: absolute;
    left: 37px; top: 294px;
    width: 520px;
    margin: 0;
    font-family: 'Montserrat', sans-serif;
    font-weight: 600;
    font-size: 17px;
    line-height: 24px;
    font-variant: small-caps;
    color: var(--white);
  }
  .steps {
    position: absolute;
    left: 36px; top: 364px;
    margin: 0; padding: 0;
    list-style: none;
    font-family: 'Montserrat', sans-serif;
    font-weight: 500;
    font-size: 19px;
    line-height: 23px;
    letter-spacing: 1.8px;
    text-transform: uppercase;
    color: var(--white);
  }
  .steps li { display: flex; }
  .step-label {
    color: var(--accent-yellow);
    width: 96px;
    flex: none;
  }
  .blurbs {
    position: absolute;
    left: 40px; top: 516px;
    width: 500px;
    margin: 0;
    text-align: center;
    font-family: 'Montserrat', sans-serif;
    font-weight: 600;
    font-size: 17px;
    line-height: 23px;
    font-variant: small-caps;
    color: var(--white);
  }
  .blurbs p { margin: 0; }
  .publisher-mark {
    position: absolute;
    left: 70px; top: 822px;
    display: flex;
    align-items: center;
    gap: 10px;
    font-family: 'Oswald', sans-serif;
    font-weight: 500;
    font-size: 26px;
    color: var(--logo-navy);
  }
  .publisher-mark .mark-square {
    width: 22px; height: 22px;
    background: var(--logo-navy);
  }
  .isbn-box {
    position: absolute;
    left: 320px; top: 755px;
    width: 228px; height: 139px;
    background: var(--white);
  }

  /* ---------- Spine ---------- */
  .spine {
    position: absolute;
    left: 578px; top: 0;
    width: 43px; height: 924px;
    background: var(--spine);
  }
  .spine-title, .spine-author {
    position: absolute;
    left: 50%;
    writing-mode: vertical-rl;
    transform: translateX(-50%);
    white-space: nowrap;
    color: var(--white);
    margin: 0;
  }
  .spine-title {
    top: 58px;
    font-family: 'Oswald', sans-serif;
    font-weight: 500;
    font-size: 24px;
    letter-spacing: -0.4px;
    text-transform: uppercase;
  }
  .spine-author {
    top: 666px;
    font-family: 'Bitter', serif;
    font-weight: 700;
    font-size: 27px;
  }

  /* ---------- Front cover ---------- */
  .front-cover {
    position: absolute;
    left: 621px; top: 0;
    width: 579px; height: 924px;
  }
  .front-photo {
    position: absolute; inset: 0;
    background:
      radial-gradient(ellipse at 50% 30%, var(--front-light) 0%, var(--front-mid) 45%, var(--front-dark) 100%);
  }
  .shelf {
    position: absolute;
    left: 0; right: 0;
    top: 690px; height: 140px;
    background:
      linear-gradient(180deg, rgba(220,221,212,0) 0%, rgba(214,215,206,0.85) 45%, var(--shelf) 72%, var(--shelf-shadow) 74%, rgba(70,76,66,0.9) 100%);
  }
  .front-illustration {
    position: absolute;
    left: 0; top: 380px;
    width: 579px; height: 400px;
    background:
      radial-gradient(ellipse 34% 26% at 78% 22%, rgba(240,240,232,0.95) 0%, rgba(220,221,210,0.7) 60%, rgba(220,221,210,0) 100%),
      radial-gradient(ellipse 20% 18% at 84% 60%, rgba(224,190,70,0.75) 0%, rgba(214,196,120,0.35) 60%, rgba(214,196,120,0) 100%),
      radial-gradient(ellipse 58% 40% at 50% 52%, var(--paper-light) 0%, var(--paper-mid) 60%, rgba(200,200,186,0) 100%);
  }
  .front-title {
    position: absolute;
    left: 0; top: 0;
    width: 579px;
    margin: 0;
    font-family: 'Oswald', sans-serif;
    color: var(--title-red);
    text-transform: uppercase;
    font-weight: 600;
  }
  .front-title .line-main {
    position: absolute;
    left: 56px; width: 464px;
    top: 38px;
    text-align: center;
    font-size: 132px;
    line-height: 150px;
    letter-spacing: 3px;
  }
  .front-title .line-connector {
    position: absolute;
    left: 56px; width: 464px;
    top: 182px;
    display: flex;
    align-items: center;
    gap: 22px;
    font-size: 56px;
    line-height: 66px;
    letter-spacing: 4px;
  }
  .line-connector .rule {
    flex: 1;
    height: 9px;
    background: var(--title-red);
  }
  .front-title .line-sub {
    position: absolute;
    left: 20px; width: 539px;
    top: 252px;
    text-align: center;
    white-space: nowrap;
    font-size: 46px;
    line-height: 64px;
    letter-spacing: 1.5px;
  }
  .front-author {
    position: absolute;
    left: 0; width: 579px;
    top: 848px;
    margin: 0;
    text-align: center;
    font-family: 'Bitter', serif;
    font-weight: 700;
    font-size: 40px;
    color: var(--white);
  }
</style>
</head>
<body>
<div class="cover-wrap">

  <section class="back-cover">
    <div class="back-photo" role="img" aria-label="Photograph of a tiled bathroom wall and shelf in muted olive tones"></div>
    <h2 class="back-title">Keepers of the Crooked Teacup Order</h2>
    <p class="back-intro">This is a comedy. Well, more a satire if you are going<br>to split hairs, but stop being a smarty-pants.</p>
    <ul class="steps">
      <li><span class="step-label">Step 1 :</span><span>Start drinking.<br>This book is better that way.</span></li>
      <li><span class="step-label">Step 2 :</span><span>Go poop.</span></li>
      <li><span class="step-label">Step 3 :</span><span>?????</span></li>
      <li><span class="step-label">Step 4 :</span><span>Profit!</span></li>
    </ul>
    <div class="blurbs">
      <p>"This is a must read!"</p>
      <p>(or at least a great gag gift for your<br>best bullshitting friends and family.)</p>
      <p>"Laugh out loud funny!"</p>
      <p>"No one is safe!"</p>
    </div>
    <div class="publisher-mark"><span class="mark-square"></span><span>Tallgrove Press</span></div>
    <div class="isbn-box"></div>
  </section>

  <section class="spine">
    <p class="spine-title">Keepers of the Crooked Teacup Order</p>
    <p class="spine-author">R.J. Wollstead</p>
  </section>

  <section class="front-cover">
    <div class="front-photo" role="img" aria-label="Photograph of a pale textured wall above a bathroom shelf"></div>
    <div class="shelf" role="img" aria-label="White bathroom shelf edge"></div>
    <div class="front-illustration" role="img" aria-label="Toilet paper roll unrolled on the shelf, printed as a certificate of excellence with a gold seal"></div>
    <h1 class="front-title">
      <span class="line-main">Keepers</span>
      <span class="line-connector"><span class="rule"></span><span>Of the</span><span class="rule"></span></span>
      <span class="line-sub">Crooked Teacup Order</span>
    </h1>
    <p class="front-author">R.J. Wollstead</p>
  </section>

</div>
</body>
</html>
```